Poster of Insipirational Quotes

Attached is a list of leadership quotes from Harold Brenwick. I would like a poster made, incorporating whatever design elements you like, potentially including Harold's face, and one or more of the quotes. I intend to print this out in A3 or larger to hang on my wall.

The quotes are:

Being responsible sometimes means pissing people off.

The day soldiers stop bringing you their problems is the day you have stopped leading them.

Don't be buffaloed by experts and elites. Experts often possess more data than judgment. Elites can become so inbred that they produce hemophiliacs who bleed to death as soon as they are nicked by the real world.

Don't be afraid to challenge the pros, even in their own backyard.

Never neglect details. When everyone's mind is dulled or distracted the leader must be doubly vigilant.

You don't know what you can get away with until you try.

Keep looking below surface appearances. Don't shrink from doing so (just) because you might not like what you find.

Organization doesn't really accomplish anything. Plans don't accomplish anything, either. Theories of management don't much matter. Endeavors succeed or fail because of the people involved. Only by attracting the best people will you accomplish great deeds.

Organization charts and fancy titles count for next to nothing.

Never let your ego get so close to your position that when your position goes, your ego goes with it.

Fit no stereotypes. Don't chase the latest management fads. The situation dictates which approach best accomplishes the team's mission.

Perpetual optimism is a force multiplier.

Look for intelligence and judgment, and most critically, a capacity to anticipate, to see around corners. Also look for loyalty, integrity, a high energy drive, a balanced ego, and the drive to get things done.

Great leaders are almost always great simplifiers, who can cut through argument, debate and doubt, to offer a solution everybody can understand.

The commander in the field is always right and the rear echelon is wrong, unless proved otherwise.

Have fun in your command. Don't always run at a breakneck pace. Take leave when you've earned it: Spend time with your families. Corollary: surround yourself with people who take their work seriously, but not themselves, those who work hard and play hard.

Command is lonely.

Leadership is the art of accomplishing more than the science of management
says is possible.

I need to modify the specification based on the designs that I've seen.

Executive Office

Designer to choose colors to be used in the design.

• Quotes

```html
<!DOCTYPE html>
<html lang="en">
<head>
<meta charset="UTF-8">
<title>Leadership Quotes by Harold Brenwick</title>
<link rel="stylesheet" href="https://fonts.googleapis.com/css2?family=Lato:ital,wght@0,400;0,700;0,900;1,400;1,700;1,900&display=swap">
<style>
  :root {
    --ink: #111111;
    --text: #1c1c1c;
    --panel: #e6e6e6;
    --mark: #a9a9a9;
    --paper: #ffffff;
    --backdrop: #dcdce0;
    --photo-light: #d2d2d2;
    --photo-dark: #5c5c5c;
  }
  * { margin: 0; padding: 0; box-sizing: border-box; }
  html, body { width: 1200px; height: 1200px; overflow: hidden; }
  body {
    background: var(--backdrop);
    font-family: "Lato", sans-serif;
    color: var(--text);
  }
  .poster {
    position: absolute;
    left: 200px; top: 30px;
    width: 800px; height: 1140px;
    background: var(--paper);
  }
  .poster > * { position: absolute; }

  .title-bar {
    left: 0; top: 0; width: 392px; height: 36px;
    background: var(--ink); color: #fff;
    font-weight: 700; font-size: 15.5px; letter-spacing: 0.2px;
    display: flex; align-items: center; justify-content: center;
  }
  .frame-top { left: 403px; top: 14px; width: 391px; height: 5px; background: var(--ink); }
  .frame-right { left: 788px; top: 14px; width: 6px; height: 567px; background: var(--ink); }
  .frame-left { left: 16px; top: 579px; width: 6px; height: 544px; background: var(--ink); }
  .frame-bottom { left: 16px; top: 1117px; width: 651px; height: 6px; background: var(--ink); }

  .lead-mark {
    left: 28px; top: 24px;
    font-weight: 900; font-size: 118px; line-height: 1; color: var(--ink);
  }
  .lead-quote {
    left: 103px; top: 53px; width: 662px;
    font-style: italic; font-weight: 700; font-size: 16px; line-height: 20.6px; text-align: justify;
  }
  .lead-quote b { font-weight: 900; }

  .cell { width: 235px; height: 111px; }
  .cell.panel { background: var(--panel); }
  .cell .bracket-top {
    position: absolute; top: 0; right: 0; width: 100px; height: 20px;
    border-top: 2px solid var(--ink); border-right: 2px solid var(--ink);
  }
  .cell .bracket-bottom {
    position: absolute; bottom: 0; left: 0; width: 100px; height: 20px;
    border-bottom: 2px solid var(--ink); border-left: 2px solid var(--ink);
  }
  .cell .mark {
    position: absolute; top: -2px; right: 8px;
    font-weight: 900; font-size: 56px; line-height: 1; color: var(--mark);
  }
  .cell .copy { position: absolute; }

  .headline {
    font-weight: 900; font-size: 28px; line-height: 31px; text-align: center;
  }
  .headline .underlined { border-bottom: 3px solid #bbb; }

  .justify { text-align: justify; }
  .italic { font-style: italic; }

  .portrait {
    left: 22px; top: 770px; width: 302px; height: 347px;
    background: radial-gradient(ellipse at 45% 35%, var(--photo-light) 0%, #a8a8a8 45%, var(--photo-dark) 100%);
  }
  .closing-mark {
    left: 446px; top: 770px;
    font-weight: 900; font-size: 92px; line-height: 0.8; color: var(--ink);
  }
  .closing-quote {
    left: 338px; top: 796px; width: 190px;
    font-style: italic; font-weight: 700; font-size: 17px; line-height: 21px;
  }
  .name-line {
    left: 532px; top: 1022px; width: 248px;
    font-weight: 900; font-size: 31px; text-align: right; color: var(--ink);
  }
</style>
</head>
<body>
<main class="poster">
  <div class="title-bar">LEADERSHIP QUOTES BY HAROLD BRENWICK</div>
  <div class="frame-top"></div>
  <div class="frame-right"></div>
  <div class="frame-left"></div>
  <div class="frame-bottom"></div>

  <div class="lead-mark">“</div>
  <p class="lead-quote"><b>Have fun in your command.</b> Don't always run at a breakneck pace. Take leave when you've earned it: Spend time with your families. Corollary: surround yourself with people who take their work seriously, but not themselves, those who work hard and play hard.</p>

  <!-- Row 1 -->
  <section class="cell" style="left:39px; top:136px;">
    <span class="bracket-top"></span><span class="bracket-bottom"></span>
    <p class="copy headline" style="left:0; top:22px; width:235px;">COMMAND<br><span class="underlined">IS LONELY</span></p>
  </section>
  <section class="cell panel" style="left:288px; top:136px;">
    <p class="copy" style="left:33px; top:12px; width:185px; font-size:19px; line-height:20px; text-align:justify;"><b>Don't be afraid</b> to challenge the pros, even in their own backyard.</p>
  </section>
  <section class="cell" style="left:538px; top:136px;">
    <span class="bracket-top"></span><span class="bracket-bottom"></span><span class="mark">”</span>
    <p class="copy italic" style="left:16px; top:38px; width:190px; font-weight:700; font-size:16px; line-height:19px;">You don't know what you can get away with until you try.</p>
  </section>

  <!-- Row 2 -->
  <p style="left:48px; top:280px; width:213px; font-size:15px; line-height:19.5px;" class="justify">Organization doesn't really accomplish anything. Plans don't accomplish anything, either. Theories of management don't much matter. Endeavors succeed or fail because of the people involved. <b>Only by attracting the best people will you accomplish great deeds.</b></p>
  <section class="cell panel" style="left:288px; top:261px;">
    <p class="copy" style="left:0; top:34px; width:235px; font-weight:900; font-size:17.5px; line-height:23px; text-align:center;">PERPETUAL OPTIMISM IS<br>A FORCE MULTIPLIER</p>
  </section>
  <p style="left:550px; top:270px; width:206px; font-size:14.5px; line-height:15.5px;" class="justify"><b>Great leaders are almost always great simplifiers</b>, who can cut through argument, debate and doubt, to offer a solution everybody can understand.</p>

  <section class="cell" style="left:292px; top:386px; height:113px;">
    <span class="bracket-top"></span><span class="bracket-bottom"></span><span class="mark">”</span>
    <p class="copy italic justify" style="left:11px; top:40px; width:188px; font-size:14.5px; line-height:15.5px;"><b>Never let your ego get so close to your position</b> that when your position goes, your ego goes.</p>
  </section>
  <section class="cell" style="left:540px; top:386px; height:113px;">
    <span class="bracket-top"></span><span class="bracket-bottom"></span>
    <p class="copy" style="left:0; top:36px; width:235px; font-size:16.5px; line-height:22px; text-align:center;"><b style="font-weight:900;">BEING RESPONSIBLE</b><br>sometimes means<br>pissing people off.</p>
  </section>

  <!-- Row 3 -->
  <section class="cell panel" style="left:41px; top:512px;">
    <p class="copy justify" style="left:25px; top:24px; width:194px; font-size:15.5px; line-height:20px;">Organization charts and fancy titles count for next to <b>nothing.</b></p>
  </section>
  <section class="cell panel" style="left:292px; top:512px; width:234px;">
    <p class="copy justify" style="left:16px; top:18px; width:203px; font-size:14.5px; line-height:18.5px;"><b>Never neglect details.</b> When everyone's mind is dulled or distracted the leader must be doubly vigilant.</p>
  </section>
  <p style="left:548px; top:538px; width:220px; font-weight:700; font-size:14.5px; line-height:15.5px;" class="justify">The day soldiers stop bringing you their problems is the day you have stopped leading them.</p>

  <!-- Row 4 -->
  <section class="cell" style="left:41px; top:637px;">
    <span class="bracket-top"></span><span class="bracket-bottom"></span><span class="mark">”</span>
    <p class="copy italic justify" style="left:15px; top:48px; width:196px; font-weight:700; font-size:13px; line-height:16px;">The commander in the field is always right and the rear echelon is wrong, unless proved otherwise.</p>
  </section>
  <section class="cell" style="left:292px; top:637px;">
    <span class="bracket-top"></span><span class="bracket-bottom"></span>
    <p class="copy justify" style="left:17px; top:20px; width:203px; font-size:13px; line-height:16px;"><b>Fit no stereotypes.</b> Don't chase the latest management fads. The situation dictates which approach best accomplishes the team's mission.</p>
  </section>
  <p style="left:553px; top:622px; width:214px; font-size:13px; line-height:16px;" class="justify">Don't be buffaloed by experts and elites. Experts often possess more data than judgment. Elites can become so inbred that they produce hemophiliacs who bleed to death as soon as they are nicked by the real world.</p>

  <!-- Bottom -->
  <div class="portrait" role="img" aria-label="Greyscale portrait of Harold Brenwick gesturing with his hands"></div>
  <div class="closing-mark">”</div>
  <p class="closing-quote">Leadership is<br>the art of accomplishing more than the science of management says is possible.</p>

  <section class="cell panel" style="left:545px; top:752px; height:92px;">
    <p class="copy italic justify" style="left:11px; top:10px; width:213px; font-weight:700; font-size:14.5px; line-height:18.5px;">Keep looking below surface appearances. Don't shrink from doing so (just) because you might not like what you find.</p>
  </section>
  <section class="cell panel" style="left:545px; top:854px; height:130px;">
    <p class="copy justify" style="left:12px; top:8px; width:211px; font-size:13.5px; line-height:16px;"><b>Look for intelligence and judgement</b>, and most critically, a capacity to anticipate, to see around corners. Also look for <b>loyalty, integrity, a high energy drive, a balanced ego, and the drive to get things done.</b></p>
  </section>

  <div class="name-line">Harold Brenwick</div>
</main>
</body>
</html>
```